Oral Surgery Office Referral Forms and Stationary Designs

I want something like the ones you made for Harlow Crest Oral Surgery. Please use my logo for color scheme and refer to this URL:

https://www.plenmarket.example/design/204517

I would also like similar business cards with appointment date/time as well as stationaries.

Target Market(s)

Referring dentists

Industry/Entity Type

Office

Font styles to use
Serif

Requirements
Must have
• same as harlow crest oral surgery forms, I will add or delete items as I find fit once the design is ready

```html
<!DOCTYPE html>
<html lang="en">
<head>
<meta charset="utf-8">
<title>Dr. Vellano – Appointment and Business Card</title>
<link rel="stylesheet" href="https://fonts.googleapis.com/css2?family=Lato:wght@300;400;700&display=swap">
<style>
  :root {
    --stage: #1c1c1c;
    --charcoal: #3b3b3b;
    --charcoal-deep: #2d2d2d;
    --mint: #2bdc8e;
    --mint-dark: #1fbf78;
    --paper: #ffffff;
    --ink: #2a2a2a;
    --rule: #444444;
    --hint: #b5b5b5;
  }
  * { box-sizing: border-box; margin: 0; padding: 0; }
  html, body { width: 1200px; height: 896px; overflow: hidden; }
  body {
    background: var(--stage);
    font-family: "Lato", "Helvetica Neue", Arial, sans-serif;
    position: relative;
  }
  .card {
    position: absolute;
    width: 640px;
    height: 366px;
    border-radius: 18px;
    overflow: hidden;
    box-shadow: 0 14px 36px rgba(0,0,0,.55);
  }
  .card svg.backdrop { position: absolute; inset: 0; width: 100%; height: 100%; }

  /* Appointment side */
  .appointment { left: 60px; top: 50px; background: var(--paper); color: var(--ink); }
  .appointment-title {
    position: absolute; left: 30px; top: 22px;
    color: var(--paper); font-size: 26px; font-weight: 300; letter-spacing: .3px;
  }
  .form-fields { position: absolute; left: 30px; top: 122px; width: 360px; }
  .field { display: flex; align-items: flex-end; height: 36px; font-size: 13px; }
  .field-label { white-space: nowrap; padding-right: 6px; padding-bottom: 3px; }
  .field-line { flex: 1; border-bottom: 1px solid var(--rule); height: 20px; }
  .date-part {
    flex: 1; border-bottom: 1px solid var(--rule); height: 20px;
    font-size: 8px; color: var(--hint); text-align: center; line-height: 26px;
  }
  .date-sep { color: var(--hint); padding: 0 4px 3px; font-size: 12px; }
  .ampm { display: flex; gap: 8px; padding-left: 8px; padding-bottom: 3px; font-size: 12px; align-items: center; }
  .box {
    display: inline-block; width: 10px; height: 10px;
    border: 1px solid var(--mint-dark); margin-right: 3px; vertical-align: -1px;
  }
  .day-picker { position: absolute; left: 412px; top: 104px; font-size: 12px; }
  .day-picker-label { font-size: 13px; margin-bottom: 6px; }
  .day-grid { display: grid; grid-template-columns: repeat(3, auto); gap: 6px 14px; }
  .comments { position: absolute; left: 412px; top: 186px; width: 200px; }
  .comments-label { font-size: 13px; margin-bottom: 6px; }
  .comments-box { height: 110px; border: 1px solid var(--ink); }

  /* Front side */
  .front { left: 500px; top: 480px; background: linear-gradient(160deg, var(--charcoal) 0%, var(--charcoal-deep) 100%); color: var(--paper); }
  .brand { position: absolute; left: 40px; top: 40px; display: flex; gap: 14px; align-items: flex-start; }
  .brand-mark { width: 22px; height: 22px; border-radius: 50%; background: var(--mint); margin-top: 12px; }
  .brand-name { font-size: 40px; font-weight: 300; line-height: 40px; letter-spacing: 1px; }
  .brand-role { font-size: 20px; font-weight: 300; margin-top: 6px; }
  .owner { position: absolute; right: 40px; top: 44px; text-align: right; }
  .owner-name { font-size: 26px; font-weight: 700; }
  .owner-title { font-size: 15px; font-weight: 300; }
  .divider { position: absolute; left: 40px; top: 196px; width: 420px; height: 1px; background: #8a8a8a; }
  .divider-accent { position: absolute; right: 0; top: -1px; width: 150px; height: 2px; background: var(--mint); }
  .divider-dot { position: absolute; right: -4px; top: -4px; width: 8px; height: 8px; border-radius: 50%; background: var(--mint); }
  .contacts { position: absolute; left: 40px; top: 210px; list-style: none; font-size: 13px; font-weight: 300; }
  .contacts li { display: flex; align-items: center; gap: 8px; height: 21px; }
  .contacts svg { width: 12px; height: 12px; fill: var(--mint); }
  .address {
    position: absolute; right: 30px; bottom: 20px;
    display: flex; align-items: center; gap: 6px;
    font-size: 14px; color: var(--charcoal-deep);
  }
  .address svg { width: 12px; height: 14px; fill: var(--charcoal-deep); }
</style>
</head>
<body>

<section class="card appointment" aria-label="Appointment card">
  <svg class="backdrop" viewBox="0 0 640 366" preserveAspectRatio="none" aria-hidden="true">
    <path d="M0 0 H640 V14 C520 14 470 96 300 96 C200 96 90 86 0 96 Z" fill="#333"/>
    <path d="M0 96 C90 86 200 96 300 96 C470 96 520 14 640 14" fill="none" stroke="#2bdc8e" stroke-width="5"/>
  </svg>
  <h1 class="appointment-title">Appointment</h1>

  <div class="form-fields">
    <div class="field"><span class="field-label">Today's Date:</span><span class="date-part">DD</span><span class="date-sep">/</span><span class="date-part">MM</span><span class="date-sep">/</span><span class="date-part">YYYY</span></div>
    <div class="field"><span class="field-label">Appt. Date:</span><span class="date-part">DD</span><span class="date-sep">/</span><span class="date-part">MM</span><span class="date-sep">/</span><span class="date-part">YYYY</span></div>
    <div class="field"><span class="field-label">Time:</span><span class="field-line"></span><span class="ampm"><span><i class="box"></i>AM</span><span><i class="box"></i>PM</span></span></div>
    <div class="field"><span class="field-label">Patient's Name:</span><span class="field-line"></span></div>
    <div class="field"><span class="field-label">Patient's Phone Number:</span><span class="field-line"></span></div>
    <div class="field"><span class="field-label">Referred By:</span><span class="field-line"></span></div>
  </div>

  <div class="day-picker">
    <div class="day-picker-label">Day:</div>
    <div class="day-grid">
      <span><i class="box"></i>Mon</span><span><i class="box"></i>Tus</span><span><i class="box"></i>Wed</span>
      <span><i class="box"></i>Thurs</span><span><i class="box"></i>Fri</span><span><i class="box"></i>Sat</span>
      <span><i class="box"></i>Sun</span>
    </div>
  </div>

  <div class="comments">
    <div class="comments-label">Additional Comments:</div>
    <div class="comments-box"></div>
  </div>
</section>

<section class="card front" aria-label="Business card front">
  <svg class="backdrop" viewBox="0 0 640 366" preserveAspectRatio="none" aria-hidden="true">
    <path d="M170 366 C320 330 420 214 640 176" fill="none" stroke="#ffffff" stroke-width="4"/>
    <path d="M190 366 C330 334 430 226 640 190 V366 Z" fill="#2bdc8e"/>
  </svg>

  <div class="brand">
    <span class="brand-mark"></span>
    <div>
      <div class="brand-name">DR.<br>VELLANO</div>
      <div class="brand-role">Oral Surgeon</div>
    </div>
  </div>

  <div class="owner">
    <div class="owner-name">Dr. Vellano</div>
    <div class="owner-title">CEO/Founder</div>
  </div>

  <div class="divider"><span class="divider-accent"></span><span class="divider-dot"></span></div>

  <ul class="contacts">
    <li><svg viewBox="0 0 12 12" aria-hidden="true"><path d="M2.5 1 L4.5 1 L5.5 3.5 L4 4.7 C4.7 6.2 5.8 7.3 7.3 8 L8.5 6.5 L11 7.5 L11 9.5 C11 10.3 10.3 11 9.5 11 C5 11 1 7 1 2.5 C1 1.7 1.7 1 2.5 1 Z"/></svg>: +49 555-010-2040</li>
    <li><svg viewBox="0 0 12 12" aria-hidden="true"><rect x="1" y="4" width="10" height="6" rx="1"/><rect x="3" y="1" width="6" height="3"/></svg>: +49 555-010-2040</li>
    <li><svg viewBox="0 0 12 12" aria-hidden="true"><path d="M1 3 H11 V10 H1 Z M1 3 L6 7 L11 3" stroke="#2d2d2d" stroke-width=".8"/></svg>: info@drvellano.example</li>
    <li><svg viewBox="0 0 12 12" aria-hidden="true"><circle cx="6" cy="6" r="5"/><path d="M1 6 H11 M6 1 C3.5 4 3.5 8 6 11 M6 1 C8.5 4 8.5 8 6 11" stroke="#2d2d2d" stroke-width=".7" fill="none"/></svg>: www.drvellano.example</li>
  </ul>

  <div class="address">
    <svg viewBox="0 0 12 14" aria-hidden="true"><path d="M6 0 C2.7 0 0.5 2.4 0.5 5.2 C0.5 9 6 14 6 14 C6 14 11.5 9 11.5 5.2 C11.5 2.4 9.3 0 6 0 Z M6 3 A2.2 2.2 0 1 1 6 7.4 A2.2 2.2 0 1 1 6 3 Z"/></svg>
    <span>: Dr. Vellano, Lindenweg 14, 10115 Musterstadt</span>
  </div>
</section>

</body>
</html>
```